i need a business card design for my family investment company "brivo investments" based in dubai. its a diverse investment firm focusing on education, hospitality and automotive. the design has to be modern and try to incorporate the logo "E" in the design. details on card as follow

Yousef R Bin Hadrami
Managing Director
yousef@brivo.ae
www.brivo.ae

Harbor zone,falcon tower, office 3817, dubai
tel. 04 7391852
mobile.050 8142903

Target Market(s)

card used for networking events and investor meetings

Industry/Entity Type

Hospitality

```html
<!DOCTYPE html>
<html lang="en">
<head>
<meta charset="utf-8">
<title>Brivo Investments – Business Card</title>
<link rel="stylesheet" href="https://fonts.googleapis.com/css2?family=Cinzel:wght@400;700&display=swap">
<style>
  :root {
    --page-bg: #e8e5e0;
    --blue-deep: #123e78;
    --blue-mid: #1e5ea3;
    --blue-light: #5b93c9;
    --paper: #f7f7f7;
    --paper-shade: #dcdcdc;
    --ink-blue: #1f5597;
    --ink-grey: #6b6f73;
    --white: #ffffff;
  }
  * { margin: 0; padding: 0; box-sizing: border-box; }
  html, body { width: 1200px; height: 600px; overflow: hidden; }
  body {
    background: var(--page-bg);
    font-family: "Cinzel", serif;
    position: relative;
  }
  .card {
    position: absolute;
    top: 157px;
    width: 500px;
    height: 286px;
    overflow: hidden;
    box-shadow: 0 6px 18px rgba(0,0,0,0.18);
  }
  .card--back { left: 60px; background: linear-gradient(160deg, var(--white) 0%, var(--paper) 55%, var(--paper-shade) 100%); }
  .card--front { left: 640px; background: linear-gradient(150deg, var(--blue-deep) 0%, var(--blue-mid) 55%, var(--blue-light) 100%); }
  .card__shapes { position: absolute; inset: 0; }

  /* brand side */
  .front-brand {
    position: absolute;
    left: 0; right: 0; top: 50%;
    transform: translateY(-50%);
    display: flex;
    align-items: center;
    justify-content: center;
    gap: 14px;
    color: var(--white);
    font-size: 24px;
    letter-spacing: 6px;
    text-transform: uppercase;
    font-weight: 400;
    white-space: nowrap;
  }
  .front-brand__mark {
    width: 10px; height: 10px;
    background: var(--white);
    flex: none;
  }

  /* contact side */
  .back-brand {
    position: absolute;
    top: 34px; left: 0; right: 0;
    text-align: center;
    color: var(--ink-blue);
    font-size: 19px;
    letter-spacing: 5px;
    text-transform: uppercase;
    font-weight: 400;
    white-space: nowrap;
  }
  .person { position: absolute; left: 34px; top: 130px; }
  .person__name { color: var(--ink-blue); font-size: 15px; font-weight: 700; white-space: nowrap; }
  .person__title { color: var(--ink-grey); font-size: 9px; letter-spacing: 1px; text-transform: uppercase; margin-top: 4px; }
  .divider { position: absolute; left: 34px; top: 170px; width: 210px; height: 1px; background: var(--ink-grey); opacity: 0.5; }
  .contact-list { position: absolute; list-style: none; font-size: 10px; color: var(--ink-grey); }
  .contact-list li { display: flex; align-items: center; gap: 7px; margin-bottom: 5px; white-space: nowrap; }
  .contact-list svg { width: 10px; height: 10px; fill: var(--ink-blue); flex: none; }
  .contact-list--phones { left: 34px; top: 182px; }
  .contact-list--web { left: 270px; top: 118px; }
  .address {
    position: absolute; left: 198px; bottom: 12px; width: 290px;
    color: var(--white); font-size: 10px; letter-spacing: 1px; text-transform: uppercase; line-height: 1.45;
  }
</style>
</head>
<body>

<section class="card card--back" aria-label="Business card, contact side">
  <svg class="card__shapes" viewBox="0 0 500 286" aria-hidden="true">
    <defs>
      <linearGradient id="band-blue" x1="0" y1="0" x2="1" y2="0">
        <stop offset="0" stop-color="#6a9fd2"/>
        <stop offset="1" stop-color="#164a8a"/>
      </linearGradient>
      <linearGradient id="stripe-steel" x1="0" y1="0" x2="1" y2="1">
        <stop offset="0" stop-color="#9aa2a8"/>
        <stop offset="1" stop-color="#4d565d"/>
      </linearGradient>
    </defs>
    <polygon points="500,70 500,88 350,236 326,236" fill="url(#stripe-steel)"/>
    <polygon points="500,96 500,286 300,286 300,236 360,236" fill="#164a8a"/>
    <rect x="180" y="236" width="320" height="50" fill="url(#band-blue)"/>
  </svg>

  <div class="back-brand">Brivo Investments</div>

  <div class="person">
    <div class="person__name">Yousef R Bin Hadrami</div>
    <div class="person__title">Managing Director</div>
  </div>
  <div class="divider"></div>

  <ul class="contact-list contact-list--phones">
    <li><svg viewBox="0 0 10 10"><path d="M2 0h2l1 2.5-1.3 1a5 5 0 0 0 2.8 2.8l1-1.3L10 6v2a2 2 0 0 1-2 2A8 8 0 0 1 0 2a2 2 0 0 1 2-2z"/></svg>04 7391852</li>
    <li><svg viewBox="0 0 10 10"><rect x="2.5" y="0" width="5" height="10" rx="1"/></svg>050 8142903</li>
  </ul>

  <ul class="contact-list contact-list--web">
    <li><svg viewBox="0 0 10 10"><path d="M0 2h10v6H0zM0 2l5 3.5L10 2" stroke="#f7f7f7" stroke-width="0.6"/></svg>yousef@brivo.ae</li>
    <li><svg viewBox="0 0 10 10"><circle cx="5" cy="5" r="5"/></svg>www.brivo.ae</li>
  </ul>

  <p class="address">Harbor zone,falcon tower,<br>office 3817, dubai</p>
</section>

<section class="card card--front" aria-label="Business card, brand side">
  <div class="front-brand"><span class="front-brand__mark"></span>Brivo Investments</div>
</section>

</body>
</html>
```